Innovative Consulting Firm Needs New Business Cards and Stationary

Our Innovative Consulting Firm, Larkfield Consulting, is in need of new business cards and stationary designs. We want two-sided cards that incorporate our logo, which is attached. We are looking for something not too formal, but is professional and slick.

Card should have the following information:
Name (ex. Tom Bradley)
Title (ex. Manager)
Address (ex. 24680 Cedar Lane)
Address 2 (ex. Suite 100)
City
State
Zip Code
Mobile
Email

The card should also have our website: www.larkfieldconsulting.example

Industry/Entity Type

Management Consulting

Contact Information for Business Card

Name (ex. Tom Bradley)
Title (ex. Manager)
Address 2 (ex. Suite 100)
City
State
Zip Code
Mobile
Email

Font styles to use
Sans Serif

Requirements
Must have
• The colors on the card must match the colors in the logo. The exact color codes are attached in a pdf.
Nice to have
• The Company's Tagline is "Focused on your Future". This might be nice to incorporate, but not necessary.

```html
<!DOCTYPE html>
<html lang="en">
<head>
<meta charset="utf-8">
<title>Larkfield Consulting – Business Card</title>
<link rel="stylesheet" href="https://fonts.googleapis.com/css2?family=Questrial&display=swap">
<style>
  :root {
    --navy: #1b4b76;
    --gold: #e3a21a;
    --ink: #2b2b2b;
    --paper: #f4f4f4;
    --card-black: #1f1f1f;
    --logo-light: #8fb1cf;
    --backdrop: #d8d8d8;
  }
  * { margin: 0; padding: 0; box-sizing: border-box; }
  html, body { width: 1200px; height: 1029px; overflow: hidden; }
  body {
    background: radial-gradient(ellipse at 50% 35%, #f2f2f2 0%, var(--backdrop) 60%, #9e9e9e 100%);
    font-family: "Questrial", "Century Gothic", sans-serif;
    position: relative;
  }
  .card {
    position: absolute;
    width: 640px;
    height: 366px;
    border-radius: 24px;
    box-shadow: 0 18px 40px rgba(0,0,0,0.28);
    overflow: hidden;
  }
  /* front */
  .card-front {
    left: 470px; top: 110px;
    background: linear-gradient(135deg, #ffffff 0%, var(--paper) 100%);
  }
  .front-logo {
    position: absolute; left: 36px; top: 96px;
    font-size: 30px; color: var(--navy); letter-spacing: 1px;
  }
  .identity {
    position: absolute; right: 96px; top: 34px; text-align: left;
  }
  .identity-name { font-size: 26px; color: var(--ink); letter-spacing: 1px; }
  .identity-title { font-size: 17px; color: var(--navy); letter-spacing: 1px; margin-top: 2px; }
  .corner-mark {
    position: absolute; right: 26px; top: 34px;
    width: 56px; height: 38px; display: flex;
  }
  .corner-mark .bar { width: 12px; background: var(--gold); }
  .corner-mark .block { flex: 1; background: var(--navy); }
  .contact {
    position: absolute; left: 330px; top: 190px;
    list-style: none; font-size: 17px; color: var(--ink); letter-spacing: 0.8px;
  }
  .contact li { display: flex; align-items: flex-start; gap: 12px; margin-bottom: 10px; line-height: 1.25; }
  .contact svg { flex: 0 0 16px; margin-top: 2px; }
  /* back */
  .card-back {
    left: 90px; top: 570px;
    background: var(--card-black);
    display: flex; align-items: center; justify-content: center;
  }
  .back-logo {
    font-size: 52px; color: var(--logo-light); letter-spacing: 2px;
  }
</style>
</head>
<body>
  <section class="card card-front" aria-label="Business card front">
    <div class="front-logo">Larkfield Consulting</div>
    <div class="identity">
      <div class="identity-name">Tom Bradley</div>
      <div class="identity-title">Manager</div>
    </div>
    <div class="corner-mark"><span class="bar"></span><span class="block"></span></div>
    <ul class="contact">
      <li>
        <svg width="16" height="18" viewBox="0 0 16 18" aria-hidden="true"><path d="M8 1a6 6 0 0 0-6 6c0 4.5 6 10 6 10s6-5.5 6-10a6 6 0 0 0-6-6z" fill="var(--navy)"/><circle cx="8" cy="7" r="2.2" fill="#fff"/></svg>
        <span>24680 Cedar Lane, ex. Suite 100<br>City, State 0000</span>
      </li>
      <li>
        <svg width="16" height="18" viewBox="0 0 16 18" aria-hidden="true"><rect x="3" y="1" width="10" height="16" rx="2" fill="none" stroke="var(--navy)" stroke-width="2"/><circle cx="8" cy="14" r="1" fill="var(--navy)"/></svg>
        <span>000 000 0000</span>
      </li>
      <li>
        <svg width="16" height="18" viewBox="0 0 16 18" aria-hidden="true"><rect x="1" y="4" width="14" height="10" fill="var(--navy)"/><path d="M1 4l7 6 7-6" fill="none" stroke="#fff" stroke-width="1.3"/></svg>
        <span>tom@larkfieldconsulting.example</span>
      </li>
    </ul>
  </section>

  <section class="card card-back" aria-label="Business card back">
    <div class="back-logo">Larkfield Consulting</div>
  </section>
</body>
</html>
```